Kelvoro Global corporate slide deck

We are looking for a custom powerpoint template to use both internally and externally with clients and during trainings/presentations. Our customers/clients often include a lot of government agencies, and we specialize in forensics, biometrics, and identity intelligence.
Requirements:
• Title slide
• Section slide
• Title and content slide
• Every slide branded
• Every slide (other than title) includes slide number (x of y), title, and date
• Modern-looking but conservative
• Visually appealing
• Source Sans Pro font
• Call out boxes

The circle in our logo does not signify or mean anything in any way, but we also don't mind it being used as a design element. We also like pulling the blue to red gradient.
Ideally we do not want to use any images of people, but iconography is likely okay.

```html
<!DOCTYPE html>
<html lang="en">
<head>
<meta charset="utf-8">
<title>Kelvoro Global – Slide Deck Overview</title>
<link rel="stylesheet" href="https://fonts.googleapis.com/css2?family=Lexend:wght@400;500;600;700;800&family=Source+Sans+3:wght@400;600;700&display=swap">
<style>
:root{
  --board:#dcdde0;
  --ink:#2b1d6e;
  --navy:#2e1f8c;
  --crimson:#b3134b;
  --grey-text:#6d6d7a;
  --panel:#eef0ee;
  --grad:linear-gradient(90deg,#3a1f8f 0%,#b0134f 100%);
  --grad-diag:linear-gradient(115deg,#3a1ea0 0%,#7e1c86 55%,#c0124a 100%);
}
*{box-sizing:border-box}
html,body{margin:0;padding:0;overflow:hidden}
body{width:907px;height:1200px;background:var(--board);position:relative;font-family:'Source Sans 3',sans-serif}
.defs{position:absolute;width:0;height:0}
.slide{position:absolute;width:534px;height:300px;background:#fff;transform:scale(.5);transform-origin:0 0;overflow:hidden;box-shadow:5px 7px 12px rgba(0,0,0,.28)}
.slide > *{position:absolute}
.slide-title{left:17px;top:12px;margin:0;font:600 17px 'Lexend',sans-serif;color:var(--ink)}
.title-rule{left:17px;top:42px;width:34px;height:3px;background:var(--crimson)}
.corner-brand{right:12px;top:14px;font:600 10px 'Lexend',sans-serif;color:var(--ink);display:flex;align-items:center;gap:3px}
.corner-brand i{display:block;width:6px;height:6px;border-radius:50%;background:var(--crimson)}
.slide-foot{left:10px;right:10px;bottom:6px;height:12px;display:flex;align-items:flex-end;justify-content:space-between}
.slide-foot::before{content:"";position:absolute;left:0;right:16px;bottom:2px;height:1px;background:var(--grad)}
.slide-foot span{position:relative;top:-4px;font:600 3.5px 'Source Sans 3',sans-serif;color:#333;background:#fff;padding-right:3px}
.slide-foot b{position:relative;width:12px;height:12px;border:1px solid var(--navy);border-radius:50%;font:600 5px 'Lexend',sans-serif;color:var(--ink);display:flex;align-items:center;justify-content:center;background:#fff}
.tiny{font:400 4.6px/1.4 'Source Sans 3',sans-serif;color:var(--grey-text);margin:0}
.tiny.light{color:#fff}
.head{font:600 7px 'Lexend',sans-serif;color:var(--ink);margin:0}
.head.red{color:var(--crimson)}
.head.white{color:#fff}
.num-box{width:14px;height:14px;background:var(--crimson);color:#fff;font:700 8px 'Lexend',sans-serif;display:flex;align-items:center;justify-content:center}
.dot-icon{border-radius:50%;background:var(--crimson);display:flex;align-items:center;justify-content:center}
.dot-icon.navy{background:var(--navy)}
.map-fill{background:radial-gradient(ellipse at center,#eceef2 0%,#f5f6f8 60%,rgba(255,255,255,0) 100%)}
.flex-col{display:flex;flex-direction:column}
</style>
</head>
<body>

<svg class="defs" aria-hidden="true">
  <defs>
    <linearGradient id="gradBrand" x1="0" y1="0" x2="1" y2="0">
      <stop offset="0" stop-color="#3a1f8f"/><stop offset="1" stop-color="#b0134f"/>
    </linearGradient>
  </defs>
</svg>

<!-- Row 1 -->
<section class="slide" style="left:40px;top:37px">
  <div role="img" aria-label="Decorative brand ring motif in blue to red" style="left:-160px;top:-60px;width:400px;height:420px;border-radius:50%;background:radial-gradient(circle at 60% 50%,rgba(255,255,255,1) 38%,rgba(176,19,79,.12) 55%,rgba(58,31,143,.22) 70%,rgba(255,255,255,0) 72%)"></div>
  <div style="left:168px;top:136px;display:flex;align-items:center;gap:5px;font:700 24px 'Lexend',sans-serif;color:var(--ink)"><i style="display:block;width:12px;height:12px;border-radius:50%;background:var(--crimson)"></i>Kelvoro</div>
  <p style="left:280px;top:100px;margin:0;font:400 16px 'Lexend',sans-serif;color:var(--crimson)">Presentation</p>
  <p style="left:278px;top:118px;margin:0;font:700 36px/1 'Lexend',sans-serif;color:var(--ink)">Business</p>
  <p style="left:279px;top:160px;margin:0;font:600 30px/1 'Lexend',sans-serif;color:var(--ink)">Marketing</p>
  <div style="left:279px;top:208px;width:255px;height:1px;background:var(--grad)"></div>
  <p style="left:280px;top:214px;margin:0;font:400 7px 'Lexend',sans-serif;letter-spacing:2.6px;color:#333">www.kelvoroglobal.com</p>
</section>

<section class="slide" style="left:321px;top:37px;background:var(--grad-diag)">
  <div style="left:0;top:0;width:534px;height:300px;background:radial-gradient(circle at 50% 45%,rgba(255,255,255,.14) 0%,rgba(255,255,255,0) 45%)"></div>
  <div style="left:0;top:95px;width:534px;display:flex;justify-content:center;align-items:center;gap:6px;font:700 30px 'Lexend',sans-serif;color:#fff"><i style="display:block;width:12px;height:12px;border-radius:50%;background:#fff"></i>Kelvoro</div>
  <p style="left:208px;top:198px;width:118px;height:18px;margin:0;border-radius:9px;background:var(--crimson);font:400 13px/18px 'Lexend',sans-serif;color:#fff;text-align:center">Presentation</p>
  <p style="left:0;top:222px;width:534px;margin:0;text-align:center;font:700 21px 'Lexend',sans-serif;color:#fff">Business Marketing</p>
  <p style="left:0;top:257px;width:534px;margin:0;text-align:center;font:400 7px 'Lexend',sans-serif;letter-spacing:2.6px;color:#fff">www.kelvoroglobal.com</p>
</section>

<section class="slide" style="left:601px;top:37px">
  <div class="corner-brand"><i></i>Kelvoro</div>
  <div style="left:139px;top:59px;width:311px;height:197px;background:var(--panel)"></div>
  <div style="left:63px;top:118px;width:138px;height:70px;background:var(--grad);display:flex;align-items:center;justify-content:center;font:700 24px 'Lexend',sans-serif;color:#fff">Agenda</div>
  <div style="left:74px;top:114px;width:8px;height:8px;background:var(--navy)"></div>
  <div style="left:170px;top:184px;width:8px;height:8px;background:var(--crimson)"></div>
  <div class="flex-col" style="left:226px;top:78px;gap:22px">
    <div><p class="head" style="color:var(--navy)">1. Lorem ipsum</p><p class="tiny">A short note on the first topic we will cover.<br>Key points and goals</p></div>
    <div><p class="head" style="color:var(--navy)">2. Lorem ipsum</p><p class="tiny">A short note on the second topic we will cover.<br>Key points and goals</p></div>
    <div><p class="head" style="color:var(--navy)">3. Lorem ipsum</p><p class="tiny">A short note on the third topic we will cover.<br>Key points and goals</p></div>
    <div><p class="head" style="color:var(--navy)">4. Lorem ipsum</p><p class="tiny">A short note on the final topic we will cover.<br>Key points and goals</p></div>
  </div>
  <footer class="slide-foot"><span>© 2024 Kelvoro Global. All rights reserved.</span><b>2</b></footer>
</section>

<!-- Row 2 -->
<section class="slide" style="left:40px;top:200px">
  <h2 class="slide-title">Text Added Here</h2><span class="title-rule"></span>
  <div class="corner-brand"><i></i>Kelvoro</div>
  <div class="flex-col" style="left:56px;top:78px;gap:24px;width:225px">
    <div><p class="head"><span style="color:var(--crimson)">01.</span>&nbsp; Aliquam Erat Volutpat</p><p class="tiny" style="padding-left:20px">A brief line of text that supports this point well.<br>Second line of supporting detail.</p></div>
    <div><p class="head"><span style="color:var(--crimson)">02.</span>&nbsp; Consectetuer Adipiscing Elit</p><p class="tiny" style="padding-left:20px">A brief line of text that supports this point well.<br>Second line of supporting detail.</p></div>
    <div><p class="head"><span style="color:var(--crimson)">03.</span>&nbsp; Duis Autem Vel Eum</p><p class="tiny" style="padding-left:20px">A brief line of text that supports this point well.<br>Second line of supporting detail.</p></div>
    <div><p class="head"><span style="color:var(--crimson)">04.</span>&nbsp; Aliquam Erat Volutpat</p><p class="tiny" style="padding-left:20px">A brief line of text that supports this point well.<br>Second line of supporting detail.</p></div>
  </div>
  <div style="left:292px;top:74px;width:171px;height:178px;background:var(--grad)"></div>
  <div class="dot-icon" style="left:274px;top:89px;width:36px;height:36px;border:2px solid #fff"><svg width="16" height="14" viewBox="0 0 16 14"><rect x="1" y="1" width="14" height="9" rx="1" fill="none" stroke="#fff" stroke-width="1.4"/><path d="M5 13h6M8 10v3" stroke="#fff" stroke-width="1.4"/></svg></div>
  <div class="dot-icon" style="left:274px;top:143px;width:36px;height:36px;border:2px solid #fff"><svg width="16" height="14" viewBox="0 0 16 14"><path d="M3 9a4 4 0 0 1 1-7 5 5 0 0 1 9 2 3 3 0 0 1 0 5z" fill="none" stroke="#fff" stroke-width="1.4"/><path d="M8 9v4" stroke="#fff" stroke-width="1.4"/></svg></div>
  <div class="dot-icon" style="left:274px;top:200px;width:36px;height:36px;border:2px solid #fff"><svg width="16" height="14" viewBox="0 0 16 14"><path d="M2 11l4-5 4 3 4-6" fill="none" stroke="#fff" stroke-width="1.4"/><circle cx="2" cy="11" r="1.4" fill="#fff"/><circle cx="6" cy="6" r="1.4" fill="#fff"/><circle cx="10" cy="9" r="1.4" fill="#fff"/><circle cx="14" cy="3" r="1.4" fill="#fff"/></svg></div>
  <div class="flex-col" style="left:324px;top:89px;gap:20px;width:125px">
    <div><p class="head white">Lorem ipsum</p><p class="tiny light">Brief supporting text for this callout, kept short and clear.</p></div>
    <div><p class="head white">Lorem ipsum</p><p class="tiny light">Brief supporting text for this callout, kept short and clear.</p></div>
    <div><p class="head white">Lorem ipsum</p><p class="tiny light">Brief supporting text for this callout, kept short and clear.</p></div>
  </div>
  <footer class="slide-foot"><span>© 2024 Kelvoro Global. All rights reserved.</span><b>3</b></footer>
</section>

<section class="slide" style="left:321px;top:200px">
  <h2 class="slide-title">Text Added Here</h2><span class="title-rule"></span>
  <div class="corner-brand"><i></i>Kelvoro</div>
  <div class="map-fill" role="img" aria-label="Faint world map backdrop" style="left:70px;top:48px;width:394px;height:170px"></div>
  <div style="left:97px;top:74px;width:88px;height:140px;border:3px solid var(--navy);border-radius:8px;padding:18px 8px 0;text-align:center">
    <p class="head" style="color:var(--crimson);font-size:12px">&#9711;</p><p class="head" style="margin:3px 0 4px">IDEA</p><p class="tiny">Short text that explains this first stage of the plan in a few clear words.</p></div>
  <div style="left:219px;top:74px;width:90px;height:140px;border:3px solid var(--navy);border-radius:8px;padding:18px 8px 0;text-align:center">
    <p class="head" style="color:var(--crimson);font-size:12px">&#9993;</p><p class="head" style="margin:3px 0 4px">PROMOTION</p><p class="tiny">Short text that explains this second stage of the plan in a few clear words.</p></div>
  <div style="left:342px;top:74px;width:91px;height:140px;border:3px solid var(--navy);border-radius:8px;padding:18px 8px 0;text-align:center">
    <p class="head" style="color:var(--crimson);font-size:12px">&#8599;</p><p class="head" style="margin:3px 0 4px">GROWTH</p><p class="tiny">Short text that explains this third stage of the plan in a few clear words.</p></div>
  <div class="dot-icon navy" style="left:181px;top:108px;width:9px;height:9px"></div>
  <div class="dot-icon navy" style="left:304px;top:108px;width:9px;height:9px"></div>
  <p class="tiny" style="left:60px;top:233px;width:414px;text-align:center">A closing summary that ties the three stages together and explains how each one leads into the next, keeping the message focused on the outcome for the client and the team.</p>
  <footer class="slide-foot"><span>© 2024 Kelvoro Global. All rights reserved.</span><b>4</b></footer>
</section>

<section class="slide" style="left:601px;top:200px">
  <h2 class="slide-title">Text Added Here</h2><span class="title-rule"></span>
  <div class="corner-brand"><i></i>Kelvoro</div>
  <div class="flex-col" style="left:40px;top:66px;width:466px;gap:12px">
    <div><p class="head" style="margin-bottom:3px">1. Text Added Here</p><p class="tiny">This paragraph gives an overview of the first key area, describing the approach, the people involved and the expected results for each stage of the work. It explains how the team will measure progress and report back to stakeholders on a regular basis. It also notes the main risks and how they will be managed over time.</p></div>
    <div><p class="head" style="margin-bottom:3px">2. Text Added Here</p><p class="tiny">This paragraph gives an overview of the second key area, describing the approach, the people involved and the expected results for each stage of the work. It explains how the team will measure progress and report back to stakeholders on a regular basis. It also notes the main risks and how they will be managed over time.</p></div>
    <div><p class="head" style="margin-bottom:3px">3. Text Added Here</p><p class="tiny">This paragraph gives an overview of the third key area, describing the approach, the people involved and the expected results for each stage of the work. It explains how the team will measure progress and report back to stakeholders on a regular basis. It also notes the main risks and how they will be managed over time.</p></div>
  </div>
  <footer class="slide-foot"><span>© 2024 Kelvoro Global. All rights reserved.</span><b>5</b></footer>
</section>

<!-- Row 3 -->
<section class="slide" style="left:40px;top:364px">
  <h2 class="slide-title">Text Added Here</h2><span class="title-rule"></span>
  <div class="corner-brand"><i></i>Kelvoro</div>
  <div style="left:51px;top:66px;width:198px"><p class="head" style="margin-bottom:4px">1. Text Added Here</p><p class="tiny">A short paragraph that outlines the first column topic, with a few lines of context about scope, timing and the team that supports it.</p><p class="tiny" style="margin-top:5px">A second paragraph adds more detail on the method and the results we expect to see over the next period of work.</p></div>
  <div style="left:273px;top:66px;width:198px"><p class="head" style="margin-bottom:4px">2. Text Added Here</p><p class="tiny">A short paragraph that outlines the second column topic, with a few lines of context about scope, timing and the team that supports it.</p><p class="tiny" style="margin-top:5px">A second paragraph adds more detail on the method and the results we expect to see over the next period of work.</p></div>
  <div class="num-box" style="left:65px;top:188px">1.</div><div style="left:92px;top:187px;width:130px"><p class="head" style="color:var(--navy)">Lorem ipsum</p><p class="tiny">Short supporting note for this item, kept brief.</p></div>
  <div class="num-box" style="left:65px;top:235px">2.</div><div style="left:92px;top:234px;width:130px"><p class="head" style="color:var(--navy)">Lorem ipsum</p><p class="tiny">Short supporting note for this item, kept brief.</p></div>
  <div class="num-box" style="left:292px;top:186px">1.</div><div style="left:320px;top:185px;width:130px"><p class="head" style="color:var(--navy)">Lorem ipsum</p><p class="tiny">Short supporting note for this item, kept brief.</p></div>
  <div class="num-box" style="left:292px;top:233px">2.</div><div style="left:320px;top:232px;width:130px"><p class="head" style="color:var(--navy)">Lorem ipsum</p><p class="tiny">Short supporting note for this item, kept brief.</p></div>
  <footer class="slide-foot"><span>© 2024 Kelvoro Global. All rights reserved.</span><b>6</b></footer>
</section>

<section class="slide" style="left:321px;top:364px">
  <div style="left:20px;top:17px;width:490px;height:264px;background:linear-gradient(160deg,#3b1fa0 0%,#2a1a88 55%,#1f177a 100%)"></div>
  <div style="left:178px;top:65px;width:170px;height:170px;border-radius:50%;border:3px solid var(--crimson);padding:6px">
    <div style="width:100%;height:100%;border-radius:50%;background:var(--crimson);display:flex;flex-direction:column;align-items:center;justify-content:center;text-align:center">
      <p style="margin:0;font:700 30px/1 'Lexend',sans-serif;color:#fff">Section<br>Break</p>
      <p class="tiny light" style="width:100px;margin-top:6px;font-size:4px">Short line that introduces the next section of the deck.</p>
    </div>
  </div>
</section>

<section class="slide" style="left:601px;top:364px">
  <h2 class="slide-title">Text Added Here</h2><span class="title-rule"></span>
  <div class="corner-brand"><i></i>Kelvoro</div>
  <p class="head" style="left:0;top:72px;width:534px;text-align:center;font-size:13px;font-weight:500">Text Added</p>
  <p class="tiny" style="left:70px;top:94px;width:394px;text-align:center">A centered paragraph that frames the key figures below, giving the audience context on where the numbers come from and why they matter to the program.</p>
  <p class="tiny" style="left:70px;top:127px;width:394px;text-align:center">A second centered paragraph adds one more layer of detail on the period covered and the sources used for each of the results.</p>
  <div style="left:69px;top:165px;width:379px;height:77px;background:var(--grad);display:flex;padding:11px 18px;gap:10px">
    <div style="flex:1;border-right:1px solid rgba(255,255,255,.3)"><p style="margin:0;font:700 17px 'Lexend',sans-serif;color:#fff">768K</p><p class="head white">Lorem Ipsum</p><p class="tiny light">Short note on this figure.</p></div>
    <div style="flex:1;border-right:1px solid rgba(255,255,255,.3)"><p style="margin:0;font:700 17px 'Lexend',sans-serif;color:#fff">423K</p><p class="head white">Lorem Ipsum</p><p class="tiny light">Short note on this figure.</p></div>
    <div style="flex:1"><p style="margin:0;font:700 17px 'Lexend',sans-serif;color:#fff">135K</p><p class="head white">Lorem Ipsum</p><p class="tiny light">Short note on this figure.</p></div>
  </div>
  <footer class="slide-foot"><span>© 2024 Kelvoro Global. All rights reserved.</span><b>8</b></footer>
</section>

<!-- Row 4 -->
<section class="slide" style="left:40px;top:527px">
  <div class="corner-brand"><i></i>Kelvoro</div>
  <p style="left:27px;top:20px;margin:0;font:600 16px/1.1 'Lexend',sans-serif;color:var(--ink)">Market<br>Opportunities.</p>
  <div style="left:27px;top:77px;width:34px;height:3px;background:var(--crimson)"></div>
  <div style="left:0;top:97px;width:184px;height:149px;background:var(--grad);padding:10px 22px 0 24px"><p style="margin:0;font:400 7.6px/1.25 'Source Sans 3',sans-serif;color:#fff">A short callout that describes the market opportunity in plain words, noting the size of the need, the main buyers and the reasons our work is well placed to meet it over the next two years and beyond.</p></div>
  <p style="left:220px;top:33px;margin:0;font:400 7px 'Lexend',sans-serif;color:#444">CONSECTETUER ADIPISCING</p>
  <svg style="left:210px;top:50px" width="290" height="145" viewBox="0 0 290 145">
    <g font-family="Lexend, sans-serif" font-size="7" fill="#333" text-anchor="end">
      <text x="14" y="10">60</text><text x="14" y="30">50</text><text x="14" y="50">40</text><text x="14" y="70">30</text><text x="14" y="90">20</text><text x="14" y="110">10</text><text x="14" y="130">0</text>
    </g>
    <g stroke="#bbb" stroke-width=".6">
      <line x1="20" y1="8" x2="285" y2="8"/><line x1="20" y1="28" x2="285" y2="28"/><line x1="20" y1="48" x2="285" y2="48"/><line x1="20" y1="68" x2="285" y2="68"/><line x1="20" y1="88" x2="285" y2="88"/><line x1="20" y1="108" x2="285" y2="108"/><line x1="20" y1="128" x2="285" y2="128"/><line x1="285" y1="8" x2="285" y2="128"/><line x1="20" y1="8" x2="20" y2="128"/>
    </g>
    <rect x="40" y="18" width="30" height="110" fill="var(--navy)"/>
    <rect x="96" y="64" width="30" height="64" fill="var(--crimson)"/>
    <rect x="152" y="34" width="30" height="94" fill="var(--navy)"/>
    <rect x="208" y="74" width="30" height="54" fill="var(--crimson)"/>
    <g font-family="Lexend, sans-serif" font-size="7" fill="#333" text-anchor="middle"><text x="55" y="140">JAN</text><text x="111" y="140">FEB</text><text x="167" y="140">MAR</text><text x="223" y="140">APR</text></g>
  </svg>
  <div style="left:218px;top:217px;width:130px"><p class="head" style="color:var(--navy)"><span style="color:var(--crimson)">&#9679;</span> Lorem Ipsum</p><p class="tiny" style="padding-left:12px">Short legend note that explains this series of data.</p></div>
  <div style="left:366px;top:217px;width:130px"><p class="head" style="color:var(--navy)"><span style="color:var(--crimson)">&#9679;</span> Lorem Ipsum</p><p class="tiny" style="padding-left:12px">Short legend note that explains this series of data.</p></div>
  <footer class="slide-foot"><span>© 2024 Kelvoro Global. All rights reserved.</span><b>11</b></footer>
</section>

<section class="slide" style="left:321px;top:527px">
  <h2 class="slide-title">Text Added Here</h2><span class="title-rule"></span>
  <div class="corner-brand"><i></i>Kelvoro</div>
  <div style="left:65px;top:85px;width:86px;height:119px;border:1.5px solid var(--crimson);border-top:2px solid var(--navy);padding:22px 7px 0"><p class="head" style="color:var(--navy)">Lorem ipsum</p><p class="tiny">Short text that sits in this card to describe one feature.</p><p class="tiny" style="margin-top:5px">A second short note to add a little more detail here.</p></div>
  <div style="left:167px;top:85px;width:86px;height:119px;border:1.5px solid var(--crimson);border-top:2px solid var(--navy);padding:22px 7px 0"><p class="head" style="color:var(--navy)">Lorem ipsum</p><p class="tiny">Short text that sits in this card to describe one feature.</p><p class="tiny" style="margin-top:5px">A second short note to add a little more detail here.</p></div>
  <div style="left:268px;top:85px;width:86px;height:119px;border:1.5px solid var(--crimson);border-top:2px solid var(--navy);padding:22px 7px 0"><p class="head" style="color:var(--navy)">Lorem ipsum</p><p class="tiny">Short text that sits in this card to describe one feature.</p><p class="tiny" style="margin-top:5px">A second short note to add a little more detail here.</p></div>
  <div style="left:369px;top:85px;width:86px;height:119px;border:1.5px solid var(--crimson);border-top:2px solid var(--navy);padding:22px 7px 0"><p class="head" style="color:var(--navy)">Lorem ipsum</p><p class="tiny">Short text that sits in this card to describe one feature.</p><p class="tiny" style="margin-top:5px">A second short note to add a little more detail here.</p></div>
  <div class="dot-icon" style="left:95px;top:71px;width:26px;height:26px;border:2px solid #fff"><svg width="12" height="10"><rect x="1" y="1" width="10" height="8" fill="none" stroke="#fff" stroke-width="1.2"/></svg></div>
  <div class="dot-icon navy" style="left:197px;top:71px;width:26px;height:26px;border:2px solid #fff"><svg width="12" height="10"><rect x="1" y="1" width="10" height="6" fill="none" stroke="#fff" stroke-width="1.2"/><path d="M4 9h4" stroke="#fff"/></svg></div>
  <div class="dot-icon" style="left:298px;top:71px;width:26px;height:26px;border:2px solid #fff"><svg width="12" height="10"><path d="M1 4l5-3 5 3-5 3z" fill="#fff"/><path d="M3 6v2h6V6" stroke="#fff" fill="none"/></svg></div>
  <div class="dot-icon navy" style="left:399px;top:71px;width:26px;height:26px;border:2px solid #fff"><svg width="12" height="10"><rect x="1" y="2" width="10" height="7" fill="none" stroke="#fff" stroke-width="1.2"/><path d="M3 7l2-2 2 1 2-3" stroke="#fff" fill="none"/></svg></div>
  <p style="left:66px;top:221px;margin:0;font:600 15px 'Lexend',sans-serif;color:var(--ink)">+ 35k</p>
  <p class="tiny" style="left:66px;top:243px;width:300px">A closing line that explains the headline figure and where it comes from in the current reporting year.</p>
  <footer class="slide-foot"><span>© 2024 Kelvoro Global. All rights reserved.</span><b>11</b></footer>
</section>

<section class="slide" style="left:601px;top:527px">
  <h2 class="slide-title">Text Added Here</h2><span class="title-rule"></span>
  <div class="corner-brand"><i></i>Kelvoro</div>
  <p class="tiny" style="left:16px;top:60px;width:205px">A short paragraph that introduces the trend shown in the chart below, with a few words on the period covered, the source of the data and the main change from one decade to the next.</p>
  <svg style="left:28px;top:130px" width="180" height="130" viewBox="0 0 180 130">
    <g font-family="Lexend, sans-serif" font-size="7" fill="#333" text-anchor="end"><text x="20" y="12">50%</text><text x="20" y="32">40%</text><text x="20" y="52">30%</text><text x="20" y="72">20%</text><text x="20" y="92">10%</text></g>
    <g stroke="#333" stroke-width=".8"><line x1="26" y1="5" x2="26" y2="110"/><line x1="26" y1="110" x2="170" y2="110"/><line x1="22" y1="10" x2="26" y2="10"/><line x1="22" y1="30" x2="26" y2="30"/><line x1="22" y1="50" x2="26" y2="50"/><line x1="22" y1="70" x2="26" y2="70"/><line x1="22" y1="90" x2="26" y2="90"/></g>
    <rect x="52" y="8" width="12" height="102" fill="var(--navy)"/>
    <rect x="85" y="48" width="12" height="62" fill="var(--crimson)"/>
    <rect x="117" y="86" width="12" height="24" fill="var(--navy)"/>
    <rect x="150" y="100" width="12" height="10" fill="var(--crimson)"/>
    <g font-family="Lexend, sans-serif" font-size="7" fill="#333" text-anchor="middle"><text x="58" y="124">1980</text><text x="91" y="124">1990</text><text x="123" y="124">2000</text><text x="156" y="124">2010</text></g>
  </svg>
  <svg style="left:273px;top:30px" width="200" height="190" viewBox="0 0 200 190">
    <circle cx="100" cy="92" r="88" fill="none" stroke="#eee" stroke-width="5"/>
    <circle cx="100" cy="92" r="88" fill="none" stroke="var(--navy)" stroke-width="5" pathLength="100" stroke-dasharray="68 100" transform="rotate(-90 100 92)"/>
    <circle cx="100" cy="92" r="78" fill="none" stroke="#eee" stroke-width="5"/>
    <circle cx="100" cy="92" r="78" fill="none" stroke="var(--crimson)" stroke-width="5" pathLength="100" stroke-dasharray="45 100" transform="rotate(-90 100 92)"/>
    <circle cx="100" cy="92" r="68" fill="none" stroke="#eee" stroke-width="5"/>
    <circle cx="100" cy="92" r="68" fill="none" stroke="var(--navy)" stroke-width="5" pathLength="100" stroke-dasharray="35 100" transform="rotate(-90 100 92)"/>
    <circle cx="100" cy="92" r="58" fill="none" stroke="#eee" stroke-width="5"/>
    <circle cx="100" cy="92" r="58" fill="none" stroke="var(--crimson)" stroke-width="5" pathLength="100" stroke-dasharray="15 100" transform="rotate(-90 100 92)"/>
    <text x="100" y="96" text-anchor="middle" font-family="Lexend, sans-serif" font-size="12" font-weight="500" fill="var(--ink)">Add Text</text>
    <g font-family="Lexend, sans-serif" font-size="7" font-weight="600"><text x="20" y="45" fill="var(--navy)">68%</text><text x="30" y="128" fill="var(--crimson)">45%</text><text x="100" y="158" fill="var(--navy)">35%</text><text x="150" y="126" fill="var(--crimson)">15%</text></g>
  </svg>
  <div style="left:256px;top:234px;width:110px"><p class="head" style="color:var(--navy)"><span style="color:var(--crimson)">&#9679;</span> Lorem ipsum</p><p class="tiny" style="padding-left:10px">Short legend note for this ring.</p></div>
  <div style="left:383px;top:234px;width:110px"><p class="head" style="color:var(--navy)"><span style="color:var(--crimson)">&#9679;</span> Lorem ipsum</p><p class="tiny" style="padding-left:10px">Short legend note for this ring.</p></div>
  <footer class="slide-foot"><span>© 2024 Kelvoro Global. All rights reserved.</span><b>12</b></footer>
</section>

<!-- Row 5 -->
<section class="slide" style="left:40px;top:689px">
  <h2 class="slide-title">Text Added Here</h2><span class="title-rule"></span>
  <div class="corner-brand"><i></i>Kelvoro</div>
  <div class="map-fill" role="img" aria-label="Faint world map backdrop" style="left:150px;top:55px;width:340px;height:200px"></div>
  <svg style="left:0;top:0" width="534" height="300"><path d="M190 150 L215 150 L235 112 L270 80 M190 150 L270 150 M190 150 L215 150 L235 190 L270 220" fill="none" stroke="#555" stroke-width=".8"/></svg>
  <div style="left:54px;top:87px;width:130px;height:130px;border-radius:50%;border:4px solid var(--navy);box-shadow:inset 0 0 0 5px #fff,inset 0 0 0 6px var(--crimson);display:flex;flex-direction:column;align-items:center;justify-content:center;font:700 12px/1.15 'Lexend',sans-serif;text-align:center"><span style="color:var(--navy)">CURRENT</span><span style="color:var(--crimson)">SOLUTIONS</span></div>
  <div class="dot-icon" style="left:268px;top:66px;width:28px;height:28px"><svg width="12" height="12"><circle cx="6" cy="6" r="5" fill="none" stroke="#fff"/><circle cx="6" cy="6" r="2" fill="#fff"/></svg></div>
  <div class="dot-icon" style="left:268px;top:134px;width:28px;height:28px"><svg width="12" height="12"><circle cx="6" cy="6" r="5" fill="none" stroke="#fff"/><circle cx="6" cy="6" r="2" fill="#fff"/></svg></div>
  <div class="dot-icon" style="left:268px;top:204px;width:28px;height:28px"><svg width="12" height="12"><circle cx="6" cy="6" r="5" fill="none" stroke="#fff"/><circle cx="6" cy="6" r="2" fill="#fff"/></svg></div>
  <div style="left:314px;top:64px;width:170px"><p class="head" style="color:var(--navy)">Project name</p><p class="tiny">Brief summary of this project, its goal and its current status for the team.</p></div>
  <div style="left:314px;top:132px;width:170px"><p class="head" style="color:var(--navy)">Project name</p><p class="tiny">Brief summary of this project, its goal and its current status for the team.</p></div>
  <div style="left:314px;top:202px;width:170px"><p class="head" style="color:var(--navy)">Project name</p><p class="tiny">Brief summary of this project, its goal and its current status for the team.</p></div>
  <footer class="slide-foot"><span>© 2024 Kelvoro Global. All rights reserved.</span><b>13</b></footer>
</section>

<section class="slide" style="left:321px;top:689px">
  <h2 class="slide-title">Text Added Here</h2><span class="title-rule"></span>
  <div class="corner-brand"><i></i>Kelvoro</div>
  <svg style="left:186px;top:74px" width="160" height="160" viewBox="0 0 160 160">
    <path d="M80 80 L80 2 A78 78 0 0 0 2 80 Z" fill="var(--navy)"/>
    <path d="M80 80 L158 80 A78 78 0 0 0 80 2 Z" fill="var(--crimson)"/>
    <path d="M80 80 L2 80 A78 78 0 0 0 80 158 Z" fill="var(--crimson)"/>
    <path d="M80 80 L80 158 A78 78 0 0 0 158 80 Z" fill="var(--navy)"/>
    <g fill="none" stroke="#fff" stroke-width="2"><line x1="80" y1="0" x2="80" y2="160"/><line x1="0" y1="80" x2="160" y2="80"/></g>
    <circle cx="80" cy="80" r="30" fill="#fff"/>
    <text x="80" y="77" text-anchor="middle" font-family="Lexend, sans-serif" font-weight="600" font-size="13" fill="var(--ink)">Text</text>
    <text x="80" y="92" text-anchor="middle" font-family="Lexend, sans-serif" font-weight="600" font-size="13" fill="var(--ink)">Added</text>
    <g fill="none" stroke="#fff" stroke-width="1.5"><circle cx="40" cy="40" r="7"/><circle cx="120" cy="40" r="7"/><circle cx="40" cy="120" r="7"/><circle cx="120" cy="120" r="7"/></g>
  </svg>
  <div style="left:50px;top:77px;width:120px;text-align:right"><p class="head red">Text Here</p><p class="tiny">Short note that explains this part of the cycle in a few words.</p></div>
  <div style="left:358px;top:77px;width:120px"><p class="head red">Text Here</p><p class="tiny">Short note that explains this part of the cycle in a few words.</p></div>
  <div style="left:50px;top:188px;width:120px;text-align:right"><p class="head red">Text Here</p><p class="tiny">Short note that explains this part of the cycle in a few words.</p></div>
  <div style="left:358px;top:188px;width:120px"><p class="head red">Text Here</p><p class="tiny">Short note that explains this part of the cycle in a few words.</p></div>
  <footer class="slide-foot"><span>© 2024 Kelvoro Global. All rights reserved.</span><b>14</b></footer>
</section>

<section class="slide" style="left:601px;top:689px">
  <div class="corner-brand"><i></i>Kelvoro</div>
  <p style="left:35px;top:28px;margin:0;font:600 16px/1.45 'Lexend',sans-serif;color:var(--ink)">Lorem Ipsum<br>Dolor Sit<br>Ametkeeper.</p>
  <div style="left:0;top:124px;width:204px;height:125px;background:var(--grad);padding:10px 18px 0 35px"><p style="margin:0;font:400 6px/1.3 'Source Sans 3',sans-serif;color:#fff">A short callout paragraph that sets out who we are and how we work with clients on every project.</p><p style="margin:8px 0 0;font:400 6px/1.3 'Source Sans 3',sans-serif;color:#fff">A second short paragraph that adds one more idea about our values and the way the team supports each client.</p></div>
  <div class="dot-icon" style="left:230px;top:50px;width:36px;height:36px"><svg width="16" height="12"><circle cx="8" cy="4" r="3" fill="#fff"/><path d="M2 12a6 5 0 0 1 12 0z" fill="#fff"/></svg></div>
  <div class="dot-icon" style="left:230px;top:120px;width:36px;height:36px"><svg width="16" height="14"><circle cx="5" cy="3" r="2" fill="#fff"/><circle cx="11" cy="3" r="2" fill="#fff"/><rect x="3" y="6" width="4" height="8" fill="#fff"/><rect x="9" y="6" width="4" height="8" fill="#fff"/></svg></div>
  <div class="dot-icon" style="left:230px;top:202px;width:36px;height:36px"><svg width="14" height="13"><path d="M7 12 L1 6 A3 3 0 0 1 7 3 A3 3 0 0 1 13 6 Z" fill="#fff"/></svg></div>
  <div style="left:293px;top:56px;width:200px"><p class="head" style="font-size:9px">We Before Me</p><p class="tiny">Short description of this value and what it means for the way we work together.</p></div>
  <div style="left:293px;top:126px;width:200px"><p class="head" style="font-size:9px">We Are Good People</p><p class="tiny">Short description of this value and what it means for the way we work together.</p></div>
  <div style="left:293px;top:208px;width:200px"><p class="head" style="font-size:9px">We Work with Heart</p><p class="tiny">Short description of this value and what it means for the way we work together.</p></div>
  <footer class="slide-foot"><span>© 2024 Kelvoro Global. All rights reserved.</span><b>15</b></footer>
</section>

<!-- Row 6 -->
<section class="slide" style="left:40px;top:851px">
  <h2 class="slide-title">Text Added Here</h2><span class="title-rule"></span>
  <div class="corner-brand"><i></i>Kelvoro</div>
  <div class="map-fill" role="img" aria-label="Faint world map backdrop" style="left:190px;top:60px;width:300px;height:190px"></div>
  <div class="num-box" style="left:36px;top:108px;width:18px;height:18px">1.</div><div style="left:64px;top:106px;width:130px"><p class="head" style="color:var(--navy)">Lorem ipsum</p><p class="tiny">Short supporting note for this point on the list.</p></div>
  <div class="num-box" style="left:36px;top:155px;width:18px;height:18px">2.</div><div style="left:64px;top:153px;width:130px"><p class="head" style="color:var(--navy)">Lorem ipsum</p><p class="tiny">Short supporting note for this point on the list.</p></div>
  <div class="num-box" style="left:36px;top:202px;width:18px;height:18px">3.</div><div style="left:64px;top:200px;width:130px"><p class="head" style="color:var(--navy)">Lorem ipsum</p><p class="tiny">Short supporting note for this point on the list.</p></div>
  <div style="left:244px;top:46px;width:60px;height:119px;border:2px solid #333;border-radius:7px;background:#fff;padding:12px 5px 0"><p class="head" style="font-size:5px;color:var(--navy)">Lorem<br>ipsum dolor</p><div style="width:14px;height:10px;margin:6px auto;border:1px solid var(--crimson)"></div><p class="tiny" style="font-size:3px">Short text about the first screen of the app.</p></div>
  <div style="left:322px;top:84px;width:60px;height:124px;border:2px solid #333;border-radius:7px;background:#fff;padding:14px 5px 0"><p class="head" style="font-size:5px;color:var(--navy)">Dolor sit<br>amet, conse</p><div style="width:12px;height:12px;margin:8px auto;border:1px solid var(--crimson);border-radius:50%"></div><p class="tiny" style="font-size:3px">Short text about the second screen of the app.</p></div>
  <div style="left:399px;top:127px;width:61px;height:125px;border:2px solid #333;border-radius:7px;background:#fff;padding:14px 5px 0"><p class="head" style="font-size:5px;color:var(--navy)">Consec</p><div style="width:12px;height:12px;margin:10px auto;border:1px solid var(--crimson);border-radius:50%"></div><p class="tiny" style="font-size:3px">Short text about the third screen of the app.</p></div>
  <footer class="slide-foot"><span>© 2024 Kelvoro Global. All rights reserved.</span><b>16</b></footer>
</section>

<section class="slide" style="left:321px;top:851px">
  <h2 class="slide-title">Text Added Here</h2><span class="title-rule"></span>
  <div class="corner-brand"><i></i>Kelvoro</div>
  <svg style="left:0;top:0" width="534" height="300">
    <polygon points="46,168 118,168 128,155 56,155" fill="var(--navy)" transform="matrix(1 0 0 -1 0 323)"/>
    <g font-family="Lexend, sans-serif" font-size="7" fill="#fff" text-anchor="middle" font-weight="500">
      <polygon points="50,155 126,155 136,168 46,168" fill="var(--navy)"/><text x="91" y="164">1990</text>
      <polygon points="132,155 218,155 228,168 140,168" fill="var(--crimson)"/><text x="180" y="164">2001</text>
      <polygon points="224,155 306,155 316,168 232,168" fill="var(--navy)"/><text x="270" y="164">2007</text>
      <polygon points="312,155 398,155 408,168 320,168" fill="var(--crimson)"/><text x="360" y="164">2012</text>
      <polygon points="404,155 478,155 488,168 412,168" fill="var(--navy)"/><text x="448" y="164">2020</text>
    </g>
    <g stroke="var(--navy)" stroke-width="1.2" fill="var(--navy)"><line x1="91" y1="130" x2="91" y2="150"/><circle cx="91" cy="130" r="2"/><line x1="262" y1="130" x2="262" y2="150"/><circle cx="262" cy="130" r="2"/><line x1="436" y1="130" x2="436" y2="150"/><circle cx="436" cy="130" r="2"/></g>
    <g stroke="var(--crimson)" stroke-width="1.2" fill="var(--crimson)"><line x1="178" y1="173" x2="178" y2="190"/><circle cx="178" cy="190" r="2"/><line x1="352" y1="173" x2="352" y2="190"/><circle cx="352" cy="190" r="2"/></g>
  </svg>
  <div style="left:51px;top:88px;width:80px;text-align:center"><p class="head" style="color:var(--navy)">Your Title</p><p class="tiny">Refers to a good or service being offered</p></div>
  <div style="left:222px;top:88px;width:80px;text-align:center"><p class="head" style="color:var(--navy)">Your Title</p><p class="tiny">Refers to a good or service being offered</p></div>
  <div style="left:396px;top:88px;width:80px;text-align:center"><p class="head" style="color:var(--navy)">Your Title</p><p class="tiny">Refers to a good or service being offered</p></div>
  <div style="left:138px;top:196px;width:80px;text-align:center"><p class="head red">Your Title</p><p class="tiny">Refers to a good or service being offered</p></div>
  <div style="left:312px;top:196px;width:80px;text-align:center"><p class="head red">Your Title</p><p class="tiny">Refers to a good or service being offered</p></div>
  <footer class="slide-foot"><span>© 2024 Kelvoro Global. All rights reserved.</span><b>17</b></footer>
</section>

<section class="slide" style="left:601px;top:851px">
  <h2 class="slide-title">Text Added Here</h2><span class="title-rule"></span>
  <div class="corner-brand"><i></i>Kelvoro</div>
  <svg style="left:0;top:0" width="534" height="300">
    <g font-family="Lexend, sans-serif" font-size="8" fill="#fff" text-anchor="middle" font-weight="500">
      <polygon points="56,104 130,104 146,127 130,150 56,150 72,127" fill="var(--navy)"/><text x="104" y="130">2024</text>
      <polygon points="138,104 212,104 228,127 212,150 138,150 154,127" fill="var(--crimson)"/><text x="186" y="130">2025</text>
      <polygon points="220,104 294,104 310,127 294,150 220,150 236,127" fill="var(--navy)"/><text x="268" y="130">2026</text>
      <polygon points="302,104 376,104 392,127 376,150 302,150 318,127" fill="var(--crimson)"/><text x="350" y="130">2027</text>
      <polygon points="384,104 460,104 476,127 460,150 384,150 400,127" fill="var(--navy)"/><text x="434" y="130">2028</text>
    </g>
  </svg>
  <div style="left:60px;top:166px;width:80px;text-align:center"><p class="head red">Project name</p><p class="tiny" style="margin-top:4px">A short line that sums up the goal for this year.</p></div>
  <div style="left:144px;top:166px;width:80px;text-align:center"><p class="head red">Project name</p><p class="tiny" style="margin-top:4px">A short line that sums up the goal for this year.</p></div>
  <div style="left:226px;top:166px;width:80px;text-align:center"><p class="head red">Project name</p><p class="tiny" style="margin-top:4px">A short line that sums up the goal for this year.</p></div>
  <div style="left:307px;top:166px;width:80px;text-align:center"><p class="head red">Project name</p><p class="tiny" style="margin-top:4px">A short line that sums up the goal for this year.</p></div>
  <div style="left:390px;top:166px;width:80px;text-align:center"><p class="head red">Project name</p><p class="tiny" style="margin-top:4px">A short line that sums up the goal for this year.</p></div>
  <footer class="slide-foot"><span>© 2024 Kelvoro Global. All rights reserved.</span><b>18</b></footer>
</section>

<!-- Row 7 -->
<section class="slide" style="left:40px;top:1013px">
  <h2 class="slide-title">Text Added Here</h2><span class="title-rule"></span>
  <div class="corner-brand"><i></i>Kelvoro</div>
  <p style="left:37px;top:92px;margin:0;font:700 26px 'Lexend',sans-serif;color:var(--ink)">The Ask<span style="color:var(--crimson)">.</span></p>
  <div style="left:50px;top:145px;width:150px"><p class="head" style="color:var(--navy)"><span style="color:var(--crimson)">&#9679;</span>&nbsp; Lorem ipsum</p><p class="tiny" style="padding-left:12px">Short note on what we are asking the audience to do next.</p></div>
  <div style="left:50px;top:193px;width:150px"><p class="head" style="color:var(--navy)"><span style="color:var(--crimson)">&#9679;</span>&nbsp; Lorem ipsum</p><p class="tiny" style="padding-left:12px">Short note on what we are asking the audience to do next.</p></div>
  <div role="img" aria-label="Desktop monitor showing the title slide" style="left:249px;top:51px;width:229px;height:192px;background:linear-gradient(180deg,#3a1e8a 0%,#8b1a6f 60%,#c9c9cf 61%,#e2e2e6 100%);border-radius:4px"></div>
  <div style="left:389px;top:186px;width:117px;height:16px;background:var(--navy);font:600 8px/16px 'Lexend',sans-serif;color:#fff;text-align:center">Text Added Here</div>
  <footer class="slide-foot"><span>© 2024 Kelvoro Global. All rights reserved.</span><b>19</b></footer>
</section>

<section class="slide" style="left:321px;top:1013px">
  <h2 class="slide-title">Text Added Here</h2><span class="title-rule"></span>
  <div class="corner-brand"><i></i>Kelvoro</div>
  <div style="left:47px;top:94px;width:78px;height:32px;background:var(--navy)"></div>
  <div style="left:163px;top:94px;width:78px;height:32px;background:var(--crimson)"></div>
  <div style="left:283px;top:94px;width:78px;height:32px;background:var(--navy)"></div>
  <div style="left:403px;top:94px;width:78px;height:32px;background:var(--crimson)"></div>
  <div role="img" aria-label="Team member portrait" style="left:66px;top:108px;width:40px;height:40px;border-radius:50%;background:linear-gradient(160deg,#d9d9de,#a9a9b2);border:2px solid #fff"></div>
  <div role="img" aria-label="Team member portrait" style="left:182px;top:108px;width:40px;height:40px;border-radius:50%;background:linear-gradient(160deg,#d9d9de,#a9a9b2);border:2px solid #fff"></div>
  <div role="img" aria-label="Team member portrait" style="left:302px;top:108px;width:40px;height:40px;border-radius:50%;background:linear-gradient(160deg,#d9d9de,#a9a9b2);border:2px solid #fff"></div>
  <div role="img" aria-label="Team member portrait" style="left:422px;top:108px;width:40px;height:40px;border-radius:50%;background:linear-gradient(160deg,#d9d9de,#a9a9b2);border:2px solid #fff"></div>
  <div style="left:42px;top:157px;width:88px;text-align:center"><p class="head red">DAREN HOLT</p><p class="tiny" style="margin-top:3px">Short bio line about this team member and the role they hold on projects.</p></div>
  <div style="left:158px;top:157px;width:88px;text-align:center"><p class="head red">INES VARGA</p><p class="tiny" style="margin-top:3px">Short bio line about this team member and the role they hold on projects.</p></div>
  <div style="left:278px;top:157px;width:88px;text-align:center"><p class="head red">DAREN HOLT</p><p class="tiny" style="margin-top:3px">Short bio line about this team member and the role they hold on projects.</p></div>
  <div style="left:398px;top:157px;width:88px;text-align:center"><p class="head red">INES VARGA</p><p class="tiny" style="margin-top:3px">Short bio line about this team member and the role they hold on projects.</p></div>
  <footer class="slide-foot"><span>© 2024 Kelvoro Global. All rights reserved.</span><b>20</b></footer>
</section>

<section class="slide" style="left:601px;top:1013px">
  <div role="img" aria-label="Decorative brand ring motif in blue to red" style="left:-150px;top:-60px;width:420px;height:420px;border-radius:50%;background:radial-gradient(circle at 58% 50%,rgba(255,255,255,1) 36%,rgba(176,19,79,.12) 54%,rgba(58,31,143,.22) 68%,rgba(255,255,255,0) 70%)"></div>
  <div style="left:160px;top:136px;display:flex;align-items:center;gap:5px;font:700 24px 'Lexend',sans-serif;color:var(--ink)"><i style="display:block;width:12px;height:12px;border-radius:50%;background:var(--crimson)"></i>Kelvoro</div>
  <p style="left:295px;top:84px;margin:0;font:700 32px 'Lexend',sans-serif;color:var(--ink)">Thank You</p>
  <svg style="left:296px;top:142px" width="16" height="100" viewBox="0 0 16 100">
    <path d="M3 2c1-1 3-1 4 1l1 2c0 1-1 2-2 2 1 2 2 3 4 4 0-1 1-2 2-2l2 1c2 1 2 3 1 4-3 2-8 0-11-4S1 4 3 2z" fill="var(--crimson)"/>
    <path d="M2 40l12-6-6 12-1-5z" fill="var(--crimson)"/>
    <path d="M8 72l7 6h-2v7H9v-4H7v4H3v-7H1z" fill="var(--crimson)"/>
  </svg>
  <div style="left:331px;top:142px;border-left:1px solid #999;padding-left:5px"><p class="tiny" style="font-size:6px;color:#555">+1 555 0142 7730<br>+1 555 0142 7731</p></div>
  <div style="left:331px;top:176px;border-left:1px solid #999;padding-left:5px"><p class="tiny" style="font-size:6px;color:#555">www.kelvoroglobal.com<br>hello@kelvoroglobal.com</p></div>
  <div style="left:331px;top:210px;border-left:1px solid #999;padding-left:5px"><p class="tiny" style="font-size:6px;color:#555">88 Harbor Lane, Fairview,<br>NY 10420, United States.</p></div>
</section>

</body>
</html>
```